Atlanta housekeeping/cleaning company needs a car wrap design for a 2019 Kalvern Hoss Tiravo Van

We need a car wrap design for a maid/housekeeping company based in Atlanta, Georgia, called BrookLark Maids. Our vehicle is a 2019 Kalvern Hoss Tiravo van with passenger configuration and rear split barn doors. Keep in mind the bumpers cannot be wrapped as they are plastic. I am open to having widows wrapped to provide additional room for the creative design. Our core values are trustworthiness, affordability, quality, thoroughness, and respect. We offer our customers the option to call or book online, so please ensure to relay that in the design. Our company promises to be eco-friendly wherever possible and we need our car wrap design to communicate this to our customers by using the color green. Please don't feel a need to include the "BrookLark Maids" text just below the logo. Get creative, and include it beside the logo, or somewhere else! I am attaching some designs I found online that I liked.

Target Market(s)

Mid to High end Housekeeping and cleaning services.

Industry/Entity Type

House Cleaning

Requirements
Must have
• Please include our email, care@brooklarkmaids.example, our phone number 1(888) 555-LARK (5275), and our website, www.brooklarkmaids.example, in your design. Thank you!

```html
<!DOCTYPE html>
<html lang="en">
<head>
<meta charset="utf-8">
<title>BrookLark Maids – Van Wrap</title>
<link rel="stylesheet" href="https://fonts.googleapis.com/css2?family=Fredoka:wght@600&family=Montserrat:wght@600;700&display=swap">
<style>
  :root {
    --green: #3cc83a;
    --green-deep: #2fae32;
    --green-text: #27b047;
    --brown: #3b2215;
    --white: #ffffff;
    --body-edge: #c9c9c9;
    --body-shade: #e9e9e9;
    --trim: #1f1f1f;
    --glass: #2a2d30;
    --tyre: #1c1c1c;
    --rim: #b9bcbf;
    --tail: #b5121b;
    --page: #e2e2e2;
  }
  html, body { margin: 0; padding: 0; overflow: hidden; background: var(--page); }
  .canvas { width: 1200px; height: 1200px; position: relative; overflow: hidden; background: var(--page); }
  .van { position: absolute; inset: 0; width: 1200px; height: 1200px; }
  .brand-name { font-family: "Fredoka", sans-serif; font-weight: 600; font-size: 27px; fill: var(--brown); }
  .contact-phone, .contact-web { font-family: "Montserrat", sans-serif; font-weight: 700; fill: var(--green-text); }
  .contact-phone { font-size: 15.5px; }
  .contact-web { font-size: 14px; }
  .contact-email { font-family: "Montserrat", sans-serif; font-weight: 600; font-size: 12px; fill: var(--white); }
</style>
</head>
<body>
<div class="canvas">
  <svg class="van" viewBox="0 0 1200 1200" xmlns="http://www.w3.org/2000/svg">
    <defs>
      <clipPath id="van-body-clip">
        <path d="M52,592 L46,540 C48,505 70,470 110,452 L250,336 C262,326 275,322 300,320 L875,310 C890,310 898,318 900,332 L925,545 L922,590 Z"/>
      </clipPath>
    </defs>
    <g transform="translate(0,-40) scale(1.25)">
      <!-- ground shadow -->
      <ellipse class="ground-shadow" cx="490" cy="632" rx="470" ry="14" fill="#bdbdbd" opacity="0.6"/>
      <!-- body -->
      <path class="van-body" fill="var(--white)" stroke="var(--body-edge)" stroke-width="1.5" d="M52,592 L46,540 C48,505 70,470 110,452 L250,336 C262,326 275,322 300,320 L875,310 C890,310 898,318 900,332 L925,545 L922,590 Z"/>
      <g clip-path="url(#van-body-clip)">
        <path class="wrap-green-sweep" fill="var(--green)" d="M0,300 L548,300 C530,360 468,410 462,478 C458,540 500,575 560,585 L660,590 L660,610 L0,610 Z"/>
        <path class="wrap-green-shade" fill="var(--green-deep)" opacity="0.35" d="M0,540 C150,560 300,570 560,585 L660,590 L660,610 L0,610 Z"/>
        <rect class="roof-shade" x="0" y="300" width="960" height="14" fill="var(--body-shade)" opacity="0.6"/>
        <path class="rear-door-line" d="M880,330 L900,560" stroke="var(--body-edge)" stroke-width="1.5" fill="none"/>
      </g>
      <!-- windows -->
      <path class="windshield" fill="var(--glass)" d="M112,452 L248,340 L262,336 L225,440 Z"/>
      <path class="side-window" fill="var(--glass)" d="M268,338 L445,326 L443,420 L268,436 C258,420 258,360 268,338 Z"/>
      <rect class="door-handle" x="385" y="440" width="46" height="9" rx="4" fill="var(--trim)"/>
      <!-- bumpers and lights -->
      <path class="front-bumper" fill="var(--trim)" d="M46,540 L130,548 L135,600 L52,596 Z"/>
      <path class="headlight" fill="var(--glass)" d="M58,480 C75,470 110,462 128,462 L118,478 C100,480 75,484 56,492 Z"/>
      <path class="rear-bumper" fill="var(--trim)" d="M840,532 L924,524 L922,592 L840,592 Z"/>
      <rect class="tail-light" x="898" y="420" width="20" height="70" rx="4" fill="var(--tail)"/>
      <!-- wheels -->
      <g class="wheel-front">
        <circle cx="178" cy="578" r="62" fill="var(--trim)"/>
        <circle cx="178" cy="578" r="52" fill="var(--tyre)"/>
        <circle cx="178" cy="578" r="33" fill="var(--rim)"/>
      </g>
      <g class="wheel-rear">
        <circle cx="745" cy="578" r="62" fill="var(--trim)"/>
        <circle cx="745" cy="578" r="52" fill="var(--tyre)"/>
        <circle cx="745" cy="578" r="33" fill="var(--rim)"/>
      </g>
      <!-- brand mark spot -->
      <circle class="brand-dot" cx="548" cy="470" r="72" fill="var(--green)"/>
      <text class="brand-name" x="625" y="386">BrookLark Maids</text>
      <text class="contact-phone" x="655" y="453">1(888) 555-LARK (5275)</text>
      <text class="contact-web" x="657" y="472" textLength="190" lengthAdjust="spacingAndGlyphs">www.brooklarkmaids.example</text>
      <text class="contact-email" x="248" y="478" textLength="192" lengthAdjust="spacingAndGlyphs">care@brooklarkmaids.example</text>
    </g>
  </svg>
</div>
</body>
</html>
```